Namecard design for Forex trading & training company

We need a design for a financial forex trading company.
Namecard should give customer a professional yet premium feel, able to differentiate from others.
1) most financial companies employs white background, while its clean and professional, it is too mainstream.
2) I am thinking of brown as base colour, however it easily gives the perception of being an Interior Design company
3) Task is to find a design that is able to portray a clean professional feel, at the same time, appear premium and differentiated from others.
*I'll be employing 3D textured print for my company namecard just so as to give it a better finishing.
Please find attached for my logo.
Financial

```html
<!DOCTYPE html>
<html lang="en">
<head>
<meta charset="UTF-8">
<title>Veltrane Capital – Business Card</title>
<link rel="stylesheet" href="https://fonts.googleapis.com/css2?family=Libre+Baskerville&family=Ubuntu:wght@400;500&display=swap">
<style>
  :root {
    --backdrop: #6a5138;
    --card-dark: #2c1800;
    --card-light: #ffffff;
    --ink-light: #ffffff;
    --ink-brand: #2b2e8c;
    --ink-body: #1e1e1e;
    --divider: #6d6d6d;
    --icon: #777777;
  }
  * { margin: 0; padding: 0; box-sizing: border-box; }
  html, body {
    width: 1200px; height: 1000px; overflow: hidden;
    background: var(--backdrop);
  }
  .canvas { position: relative; width: 1200px; height: 1000px; }
  .card {
    position: absolute; left: 293px; width: 613px; height: 360px;
    border-radius: 18px;
  }
  .card--front { top: 125px; background: var(--card-dark); }
  .card--back { top: 514px; background: var(--card-light); }

  .brand-name {
    position: absolute; left: 0; right: 0; text-align: center;
    font-family: "Libre Baskerville", serif;
    letter-spacing: 0.3em; text-transform: uppercase;
  }
  .card--front .brand-name { top: 150px; font-size: 26px; color: var(--ink-light); }
  .card--back .brand-name { top: 120px; font-size: 26px; color: var(--ink-brand); }

  .website {
    position: absolute; left: 0; right: 0; top: 317px; text-align: center;
    font-family: "Ubuntu", sans-serif; font-size: 16px; color: var(--ink-light);
  }

  .holder {
    position: absolute; left: 168px; top: 270px;
    font-family: "Ubuntu", sans-serif; color: var(--ink-body);
  }
  .holder__name { font-size: 16px; font-weight: 500; letter-spacing: -0.02em; }
  .holder__role { font-size: 14.5px; margin-top: 4px; }

  .divider {
    position: absolute; left: 306px; top: 257px; width: 1.5px; height: 82px;
    background: var(--divider);
  }

  .contact {
    position: absolute; left: 331px; top: 272px; list-style: none;
    font-family: "Ubuntu", sans-serif; font-size: 14.5px; color: var(--ink-body);
  }
  .contact__item { display: flex; align-items: center; height: 20px; }
  .contact__icon { width: 16px; height: 14px; margin-right: 7px; flex: none; }
</style>
</head>
<body>
<main class="canvas">
  <section class="card card--front">
    <div class="brand-name">Veltrane Capital</div>
    <div class="website">www.veltranecap.com</div>
  </section>

  <section class="card card--back">
    <div class="brand-name">Veltrane Capital</div>
    <div class="holder">
      <div class="holder__name">Marcus Tan</div>
      <div class="holder__role">Pantry Manager</div>
    </div>
    <div class="divider"></div>
    <ul class="contact">
      <li class="contact__item">
        <svg class="contact__icon" viewBox="0 0 16 14" aria-hidden="true">
          <rect x="5" y="0.5" width="6" height="13" rx="1" fill="none" stroke="var(--icon)" stroke-width="1.2"/>
          <rect x="6.3" y="2" width="3.4" height="3.5" fill="var(--icon)"/>
          <rect x="6.3" y="7" width="3.4" height="5" fill="var(--icon)" opacity="0.6"/>
        </svg>
        (86) 555 010 247
      </li>
      <li class="contact__item">
        <svg class="contact__icon" viewBox="0 0 16 14" aria-hidden="true">
          <rect x="1" y="2.5" width="14" height="9" fill="none" stroke="var(--icon)" stroke-width="1.1"/>
          <path d="M1 2.5 L8 8 L15 2.5" fill="none" stroke="var(--icon)" stroke-width="1.1"/>
        </svg>
        marcus@veltranecap.com
      </li>
    </ul>
  </section>
</main>
</body>
</html>
```